Young Architect Bussiness Card

English is not my first language (spanish is).
Need a bussiness card design for my best friend who is about to graduate from college, Licentiate degree in architecture, so she needs business cards to start networking, currently she has no porfolio, web page or facebook. so she is relying on her cel phone and gmail, but should leave space for one of them (facebook)

Design for business card should be modern, maybe something with construction blue prints patern or 3D modelling.

Name: Mariela Fonseca Arrieta
Licentiate in Arquitecture
Cel: (506) XXX-4827
email: marielaXXX@correovela.com

Services, although im not sure if it has to be there or not:
Anteproyectos / Proposal design
Inspecciones / Site Inspections
Modelado 3D / 3D modelling
Planos Constructivos / Construction Blue Prints
Presupuestos / Budgets

Design should be in spanish

Contact Information for Business Card

Name: Mariela Fonseca, Arquitecto
Associtation code : XXXX
Phone: (506) XXXX-XXXX
Email: xxx@correovela.com
Facebook: xxxx

Requirements
Must have
• Design for business card should be modern, maybe something with construction blue prints patern or 3D modelling.
Nice to have
• Something like a transition from 2D to 3D.

```html
<!DOCTYPE html>
<html lang="es">
<head>
<meta charset="utf-8">
<title>Tarjeta de presentación — Mariela Fonseca Arrieta</title>
<link rel="stylesheet" href="https://fonts.googleapis.com/css2?family=Open+Sans:wght@300;400;600&display=swap">
<style>
  :root {
    --page-bg: #e8f1f8;
    --card-white: #ffffff;
    --card-edge: #d9dee5;
    --ink: #2a2118;
    --ink-soft: #3a3430;
    --icon-blue: #3f6fc4;
    --blueprint: #4159a8;
    --blueprint-deep: #374d97;
    --blueprint-light: #5068b4;
    --white: #ffffff;
    --sheet-grey: #eceef1;
  }
  * { box-sizing: border-box; margin: 0; padding: 0; }
  html, body {
    width: 1200px; height: 750px; overflow: hidden;
    background: var(--page-bg);
    font-family: "Open Sans", sans-serif;
  }
  .canvas { position: relative; width: 1200px; height: 750px; }
  .card {
    position: absolute; top: 231px;
    width: 520px; height: 288px; overflow: hidden;
  }
  .card--front {
    left: 72px; background: var(--card-white);
    border: 1px solid var(--card-edge);
  }
  .card--back { left: 608px; background: var(--blueprint); }

  .front-sheet {
    position: absolute; left: 0; top: 0; width: 180px; height: 288px;
    background: linear-gradient(100deg, var(--sheet-grey) 0%, #f6f7f9 55%, rgba(255,255,255,0) 100%);
    clip-path: polygon(0 0, 100% 0, 45% 100%, 0 100%);
  }
  .holder-name {
    position: absolute; left: 291px; top: 38px; color: var(--ink);
  }
  .holder-name__surname {
    display: block; font-weight: 600; font-size: 21px; letter-spacing: 0.2px; line-height: 26px;
  }
  .holder-name__given {
    display: block; font-weight: 300; font-size: 21px; line-height: 28px;
  }
  .contact-list {
    position: absolute; top: 228px; list-style: none;
    font-weight: 300; font-size: 15.5px; color: var(--ink-soft);
  }
  .contact-list--left { left: 39px; }
  .contact-list--right { left: 291px; }
  .contact-list li { display: flex; align-items: center; height: 20px; }
  .contact-icon { width: 15px; height: 15px; margin-right: 13px; flex: none; }
  .social-square {
    width: 15px; height: 15px; margin-right: 15px; flex: none;
    background: var(--icon-blue); border-radius: 2px;
  }

  .blueprint-art {
    position: absolute; inset: 0;
    background:
      radial-gradient(ellipse at 40% 40%, var(--blueprint-light) 0%, rgba(80,104,180,0) 60%),
      linear-gradient(160deg, var(--blueprint) 0%, var(--blueprint-deep) 100%);
  }
  .services-rule {
    position: absolute; left: 322px; top: 145px; width: 1px; height: 123px;
    background: rgba(255,255,255,0.55);
  }
  .services-list {
    position: absolute; left: 342px; top: 153px; list-style: none;
    color: var(--white); font-weight: 400; font-size: 16px; line-height: 20px;
  }
</style>
</head>
<body>
<main class="canvas">
  <section class="card card--front" aria-label="Frente de la tarjeta">
    <div class="front-sheet" role="img" aria-label="Hoja de planos enrollada en tono gris tenue"></div>
    <h1 class="holder-name">
      <span class="holder-name__surname">FONSECA ARRIETA</span>
      <span class="holder-name__given">Mariela</span>
    </h1>
    <ul class="contact-list contact-list--left">
      <li>
        <svg class="contact-icon" viewBox="0 0 16 16" aria-hidden="true">
          <rect width="16" height="16" rx="2" fill="var(--icon-blue)"/>
          <path d="M4.6 3.2c.5-.3 1 0 1.3.4l.9 1.5c.2.4.1.9-.3 1.2l-.6.4c.5 1.2 1.4 2.1 2.6 2.7l.5-.6c.3-.4.8-.5 1.2-.2l1.5 1c.4.3.6.9.3 1.3l-.6.9c-.4.6-1.2.8-1.9.5C6.9 11.4 4.6 9.1 3.7 6.6c-.3-.7-.1-1.5.5-1.9z" fill="var(--white)"/>
        </svg>
        <span>(506) XXX-4827</span>
      </li>
      <li>
        <svg class="contact-icon" viewBox="0 0 16 16" aria-hidden="true">
          <rect width="16" height="16" rx="2" fill="var(--icon-blue)"/>
          <rect x="3" y="4.5" width="10" height="7" rx="1" fill="var(--white)"/>
          <path d="M3.3 5 8 8.6 12.7 5" fill="none" stroke="var(--icon-blue)" stroke-width="1"/>
        </svg>
        <span>marielaXXX@correovela.com</span>
      </li>
    </ul>
    <ul class="contact-list contact-list--right">
      <li><span class="social-square" aria-hidden="true"></span><span>mfonseca.arq</span></li>
      <li>
        <svg class="contact-icon" viewBox="0 0 16 16" aria-hidden="true">
          <rect width="16" height="16" rx="2" fill="var(--icon-blue)"/>
          <g fill="none" stroke="var(--white)" stroke-width="0.9">
            <circle cx="8" cy="8" r="5"/>
            <ellipse cx="8" cy="8" rx="2.2" ry="5"/>
            <path d="M3 8h10M4 5.5h8M4 10.5h8"/>
          </g>
        </svg>
        <span>www.fonsecaarq.com</span>
      </li>
    </ul>
  </section>

  <section class="card card--back" aria-label="Reverso de la tarjeta">
    <div class="blueprint-art" role="img" aria-label="Plano arquitectónico de una vivienda en líneas blancas sobre fondo azul"></div>
    <div class="services-rule" aria-hidden="true"></div>
    <ul class="services-list">
      <li>Anteproyectos</li>
      <li>Inspecciones</li>
      <li>Modelado 3D</li>
      <li>Planos Constructivos</li>
      <li>Presupuestos</li>
    </ul>
  </section>
</main>
</body>
</html>
```